Simple Business Cards for Self-employed Coach

Simple business card with a design that includes the QLT logo.
Using either only the logo color or additional colors that match the logo.

Meridian Guides reach deeply into the past, gathering wisdom from East and West, while still staying current with the frontiers of new discovery in cognitive science, genetics, and other disciplines. see https://www.brightharborpath.example/what-is-integral-coaching/

Target Market(s)

Coaching Clients in Tokyo /Asia; in business organizations, but also outside

Industry/Entity Type

Life Coaching

Contact Information for Business Card

Lukas Brenning
Certified Meridian Guide

3-2-48 Kamiyoshi
Nakarino 164-0392
Tokyo, Japan

Phone: +81 70 4817 5062
E-Mail: lukas.brenning@mailora.example

Font styles to use
Sans Serif

Colors
00a990

Requirements
Must have
• include uploaded logo
• color fitting with QLT logo color
Nice to have
• simple, elegant design
Should not have
• clutter

```html
<!DOCTYPE html>
<html lang="en">
<head>
<meta charset="utf-8">
<title>Lukas Brenning – Certified Meridian Guide</title>
<link rel="stylesheet" href="https://fonts.googleapis.com/css2?family=Mukta:wght@300;400;600;700&display=swap">
<style>
  :root {
    --teal: #00a990;
    --teal-deep: #137a69;
    --ink: #333333;
    --paper: #ffffff;
    --frame: #111111;
  }
  * { box-sizing: border-box; margin: 0; padding: 0; }
  html, body {
    width: 1200px;
    height: 720px;
    overflow: hidden;
    background: var(--paper);
  }
  .card {
    position: relative;
    width: 1200px;
    height: 720px;
    background: var(--paper);
    border: 2px solid var(--frame);
    overflow: hidden;
    font-family: "Mukta", sans-serif;
    color: var(--ink);
  }
  .chevron-band {
    position: absolute;
    left: 0;
    top: 0;
    width: 1200px;
    height: 720px;
  }
  .logo-panel {
    position: absolute;
    left: 48px;
    top: 265px;
    width: 443px;
    height: 192px;
    background: var(--paper);
    display: flex;
    align-items: center;
    justify-content: center;
    gap: 22px;
  }
  .logo-square {
    width: 44px;
    height: 44px;
    background: var(--teal-deep);
  }
  .logo-name {
    font-size: 92px;
    font-weight: 600;
    letter-spacing: 10px;
    color: var(--teal-deep);
    line-height: 1;
    padding-top: 10px;
  }
  .identity {
    position: absolute;
    left: 562px;
    top: 142px;
  }
  .person-name {
    font-size: 52px;
    line-height: 1;
    letter-spacing: 0.5px;
    font-weight: 300;
  }
  .person-name strong { font-weight: 700; }
  .person-title {
    margin-top: 36px;
    font-size: 31px;
    line-height: 1;
    letter-spacing: 1.5px;
    font-weight: 400;
  }
  .person-title strong { font-weight: 700; }
  .divider {
    position: absolute;
    left: 562px;
    top: 355px;
    width: 524px;
    height: 2px;
    background: var(--teal);
  }
  .contact-list {
    position: absolute;
    left: 561px;
    top: 406px;
    list-style: none;
  }
  .contact-item {
    display: flex;
    align-items: center;
    height: 42px;
    font-size: 21px;
    font-weight: 400;
  }
  .contact-icon {
    width: 32px;
    height: 32px;
    margin-right: 15px;
    flex: none;
  }
</style>
</head>
<body>
  <div class="card">
    <svg class="chevron-band" viewBox="0 0 1200 720" aria-hidden="true">
      <polygon fill="var(--teal)" points="0,0 336,0 489,265 489,457 363,720 0,720"/>
      <polygon fill="var(--paper)" points="0,267 48,352 0,459"/>
    </svg>

    <div class="logo-panel">
      <span class="logo-square"></span>
      <span class="logo-name">QLT</span>
    </div>

    <div class="identity">
      <h1 class="person-name">LUKAS <strong>BRENNING</strong></h1>
      <p class="person-title"><strong>CERTIFIED</strong> MERIDIAN GUIDE</p>
    </div>

    <div class="divider"></div>

    <ul class="contact-list">
      <li class="contact-item">
        <svg class="contact-icon" viewBox="0 0 32 32" aria-hidden="true">
          <circle cx="16" cy="16" r="16" fill="var(--ink)"/>
          <path fill="var(--paper)" d="M11 8.5l3 3.2-1.6 2.2c1 2.2 2.6 3.8 4.8 4.8l2.2-1.6 3.2 3-1.8 2.6c-5.8-.6-11.1-5.9-11.6-11.6z"/>
        </svg>
        <span>+81 70 4817 5062</span>
      </li>
      <li class="contact-item">
        <svg class="contact-icon" viewBox="0 0 32 32" aria-hidden="true">
          <circle cx="16" cy="16" r="16" fill="var(--ink)"/>
          <rect x="8" y="10.5" width="16" height="11" fill="none" stroke="var(--paper)" stroke-width="1.8"/>
          <polyline points="8,10.5 16,17 24,10.5" fill="none" stroke="var(--paper)" stroke-width="1.8"/>
        </svg>
        <span>lukas.brenning@mailora.example</span>
      </li>
      <li class="contact-item">
        <svg class="contact-icon" viewBox="0 0 32 32" aria-hidden="true">
          <circle cx="16" cy="16" r="16" fill="var(--ink)"/>
          <path fill="var(--paper)" d="M16 7a6 6 0 0 0-6 6c0 4.5 6 12 6 12s6-7.5 6-12a6 6 0 0 0-6-6zm0 8.4a2.4 2.4 0 1 1 0-4.8 2.4 2.4 0 0 1 0 4.8z"/>
        </svg>
        <span>3-2-48 Kamiyoshi, Nakarino 164-0392, Tokyo, Japan</span>
      </li>
    </ul>
  </div>
</body>
</html>
```